Redesign of Plastic Surgeon Website to fully responsive / modern feel

Hi

Our current website is out of date www.harbourlinecosmetic.org

We want a fresh / modern looking design
Needs to be fully responsive design that works extremely well on ipad and mobile device

Would like design for both full screen website and mobile

Have listed a few websites of other plastic surgeons we like
http://www.reformclinicplus.com/
http://www.doriankeelermd.com/
http://www.tarrantcontours.com/
http://www.oakdenecosmeticsurgery.com/

Menu needs to include
1. About Us
2. Procedures (see current website for example)
3. News
4. Patient Resources
5. Contact Us

We are flexible with colours / images / layout

I have uploaded a document that has some content - the face pages content is completed only

some of the procedures can have content upwards of 4000 words - total website can be large with over 40,000 words
Updates

Hi I have updated the logo for our design for the new website - this is the logo and colours we want reflected throughout the siteThanks Added Wednesday, January 13, 2016

Target Market(s)

Mainly women 20-60 85% of practice
Some men 15%

Industry/Entity Type

Plastic Surgery

Number of Pages Required

5+ page

Requirements
Must have
• We need designs for
• Homepage
• Internal pages
• 1. Landing pages for breast / body / face / non surgical main pages
• 2. Procedure pages for individual pages under each section - eg breast augmentation
• 3. About us pages - like meet the doctor, our staff, clinics
• 4. Contact page
• 5. Blog / News page
Nice to have
• See our list of websites for examples of designs we like
• Like full screen design with nice hero image
• Needs to have good to call to action messages on home page like
• Specials, procedure of the month, etc

```html
<!DOCTYPE html>
<html lang="en">
<head>
<meta charset="utf-8">
<title>Harbourline Institute of Cosmetic Surgery</title>
<link rel="stylesheet" href="https://fonts.googleapis.com/css2?family=Open+Sans:ital,wght@0,300;0,400;0,700;1,800&display=swap">
<style>
  :root {
    --plum: #7a4a7c;
    --lilac: #ab7fab;
    --ink: #1f1f1f;
    --body: #4a4a4a;
    --muted: #7a7a7a;
    --rule: #b9b9b9;
    --white: #ffffff;
    --hero-top: #b7aca8;
    --hero-bottom: #9c8c88;
  }
  * { margin: 0; padding: 0; box-sizing: border-box; }
  html, body { width: 839px; height: 1200px; overflow: hidden; background: var(--white); }
  body { position: relative; font-family: "Open Sans", sans-serif; color: var(--body); }

  .top-rule { position: absolute; top: 0; left: 0; width: 839px; height: 5px; background: var(--lilac); }

  .main-nav { position: absolute; top: 6px; left: 0; width: 839px; display: flex; justify-content: center; }
  .main-nav a { color: var(--ink); text-decoration: none; font-size: 16px; padding: 2px 17px 10px; border-left: 2px solid var(--rule); line-height: 22px; }
  .main-nav a:first-child { border-left: none; }

  .hero { position: absolute; top: 70px; left: 0; width: 839px; height: 560px;
    background: linear-gradient(180deg, var(--hero-top) 0%, var(--hero-bottom) 100%); }

  .brand { position: absolute; top: 118px; left: 0; width: 839px; text-align: center;
    color: var(--white); font-weight: 400; font-size: 32px; line-height: 56px; letter-spacing: 3px; text-transform: uppercase; }

  .enter-btn { position: absolute; top: 518px; left: 244px; width: 352px; height: 74px;
    border: 3px solid var(--white); border-radius: 37px; display: flex; align-items: center; justify-content: center;
    color: var(--white); text-decoration: none; font-weight: 800; font-style: italic; font-size: 48px; letter-spacing: 1px; }

  .intro { position: absolute; top: 686px; left: 0; width: 839px; height: 240px; }
  .intro .divider { position: absolute; left: 420px; top: 0; width: 4px; height: 240px; background: var(--lilac); }
  .column { position: absolute; top: 0; width: 260px; }
  .column.institute { left: 135px; }
  .column.doctor { left: 462px; }
  .column h2 { color: var(--plum); font-weight: 700; font-size: 35px; line-height: 42px; margin-bottom: 22px; white-space: nowrap; }
  .column p { font-size: 13px; line-height: 19px; font-weight: 400; margin-left: 3px; margin-bottom: 19px; }

  .slider-dots { position: absolute; top: 980px; left: 0; width: 839px; display: flex; justify-content: center; gap: 19px; }
  .slider-dots span { width: 64px; height: 64px; border-radius: 50%; background: var(--lilac); }

  .site-footer { position: absolute; top: 1116px; left: 0; width: 839px; height: 84px; border: 6px solid var(--lilac); }
  .footer-nav { position: absolute; top: 18px; left: 0; width: 827px; display: flex; justify-content: center; }
  .footer-nav a { color: var(--muted); text-decoration: none; font-size: 13px; line-height: 18px; padding: 2px 14px 4px; border-left: 1px solid var(--ink); }
  .footer-nav a:first-child { border-left: none; }
  .footer-bar { position: absolute; left: 54px; top: 54px; width: 720px; height: 4px; background: var(--lilac); }
</style>
</head>
<body>
  <div class="top-rule"></div>

  <nav class="main-nav">
    <a href="#">About Us</a>
    <a href="#">Procedures</a>
    <a href="#">News</a>
    <a href="#">Patient Resources</a>
    <a href="#">Contact Us</a>
  </nav>

  <section class="hero" role="img" aria-label="Full-width hero photograph for the clinic"></section>
  <div class="brand">Harbourline<br>Institute<br>of Cosmetic<br>Surgery</div>
  <a class="enter-btn" href="#">ENTER</a>

  <section class="intro">
    <div class="column institute">
      <h2>The Institute</h2>
      <p>You can expect beautiful results at the Harbourline Institute of Cosmetic Surgery.</p>
      <p>Offering unparalleled expertise in face, breast and body enhancement, including facelifts, breast augmentation / lift / reduction or tummy tucks, we offer total care at every step of your transformative journey.</p>
    </div>
    <div class="divider"></div>
    <div class="column doctor">
      <h2>Dr Whitcombe</h2>
      <p>Dr Whitcombe is one of Australia’s most eminent specialists in plastic and cosmetic surgery, and is supported by our highly qualified, professional team. As Sydney’s premier plastic surgery clinic, we use only the most revolutionary techniques to minimise scarring to help you look better, feel better and enjoy a beautiful new you.</p>
    </div>
  </section>

  <div class="slider-dots"><span></span><span></span><span></span></div>

  <footer class="site-footer">
    <nav class="footer-nav">
      <a href="#">About Us</a>
      <a href="#">Procedures</a>
      <a href="#">News</a>
      <a href="#">Patient Resources</a>
      <a href="#">Contact Us</a>
    </nav>
    <div class="footer-bar"></div>
  </footer>
</body>
</html>
```